Atelier Marrow Architecture business card

We need to update our business card. We do high end custom residential, hospitality, and wellness architecture. We focus on creating unique spaces and design around the five senses, believing that architecture's true impact is not on our surroundings, but within us. We would like to see designs are instill a sense of calm awe. They should be crisp, fresh, clean, authentic, & contemporary without being sterile, overworked, or harsh. White space is important. Alternative materials are an option if natural. We have created our own logo and would like designs to incorporate it. However, we are willing to see alternatives if the logo becomes a stumbling block and you have an alternate you suggest. Card must have the following information:
Atelier Marrow Architecture, Inc.
728 Holloway Ct. NE Atlanta, GA 30318
Marcus T. Whitcombe, AIA, NCARB, LEED AP BD+C
ateliermarrow.example

Target Market(s)

Higher net worth individuals with an appreciation for design, nature, sustainability,

Industry/Entity Type

Architect

Contact Information for Business Card

See above. The title of Owner or Architect is helpful but not necessary. Minimalism should trump additional information.

Font styles to use
Serif
Sans Serif

Requirements
Must have
• It should look professional. It must use logo
Should not have
• caligraphy, animals, anything that is cute,

```html
<!DOCTYPE html>
<html lang="en">
<head>
<meta charset="utf-8">
<title>Atelier Marrow Architecture – Business Card</title>
<link rel="stylesheet" href="https://fonts.googleapis.com/css2?family=Crimson+Pro:wght@400;500&family=Open+Sans:wght@400;700&display=swap">
<style>
  :root {
    --ink: #1e1f23;
    --sky: #c9e8ef;
    --teal: #1a8f7f;
    --slate: #45464a;
    --stone: #8c8e92;
    --paper: #ffffff;
    --text-dark: #15161a;
  }
  * { margin: 0; padding: 0; box-sizing: border-box; }
  html, body {
    width: 900px;
    height: 1200px;
    overflow: hidden;
    background: var(--paper);
  }
  .canvas {
    position: relative;
    width: 900px;
    height: 1200px;
  }
  .card {
    position: absolute;
    left: 246px;
    width: 380px;
  }
  .card--front { top: 302px; height: 231px; }
  .card--back  { top: 596px; height: 233px; }
  .card svg { display: block; width: 100%; height: 100%; }

  .fill-ink   { fill: var(--ink); }
  .fill-sky   { fill: var(--sky); }
  .fill-teal  { fill: var(--teal); }
  .fill-slate { fill: var(--slate); }
  .fill-paper { fill: var(--paper); }

  .wordmark {
    font-family: "Crimson Pro", Georgia, serif;
    font-weight: 400;
    fill: var(--stone);
    letter-spacing: 1.6px;
  }
  .wordmark__sub { letter-spacing: 2.4px; }
  .card--back .wordmark { fill: var(--slate); }

  .name-pill { fill: none; stroke: var(--paper); stroke-width: 1; }
  .name {
    font-family: "Crimson Pro", Georgia, serif;
    font-weight: 500;
    font-size: 11.5px;
    fill: var(--paper);
  }
  .address {
    font-family: "Open Sans", Arial, sans-serif;
    font-weight: 700;
    font-size: 4.6px;
    fill: var(--text-dark);
  }
  .contact-rule { stroke: var(--text-dark); stroke-width: 0.6; }
  .icon-stroke { fill: none; stroke: var(--paper); stroke-width: 0.9; stroke-linejoin: round; }
  .icon-glyph  { fill: var(--paper); }
  .icon-dark   { fill: var(--ink); }
</style>
</head>
<body>
<main class="canvas">

  <!-- Front of card -->
  <section class="card card--front" aria-label="Business card front">
    <svg viewBox="0 0 253 154" preserveAspectRatio="none">
      <rect class="fill-ink" x="0" y="0" width="253" height="154"/>
      <polygon class="fill-sky" points="0,96 55,128 80,140 130,133 175,120 253,82 253,154 0,154"/>
      <polygon class="fill-slate" points="0,96 85,118 55,140"/>
      <polygon class="fill-teal" points="55,140 68,114 100,116 80,128"/>
      <polygon class="fill-slate" points="85,118 100,116 130,133"/>
      <polygon class="fill-slate" points="130,133 175,108 182,124"/>
      <polygon class="fill-teal" points="175,108 253,82 196,104"/>

      <g class="logo">
        <text class="wordmark" x="126" y="72" text-anchor="middle" font-size="10">ATELIER MARROW</text>
        <text class="wordmark wordmark__sub" x="126" y="80" text-anchor="middle" font-size="3.4">ARCHITECTURE</text>
      </g>
    </svg>
  </section>

  <!-- Back of card -->
  <section class="card card--back" aria-label="Business card back">
    <svg viewBox="0 0 253 155" preserveAspectRatio="none">
      <rect class="fill-sky" x="0" y="0" width="253" height="155"/>
      <polygon class="fill-ink" points="113,0 253,0 253,155 142,155 150,118 172,65"/>
      <polygon class="fill-teal" points="113,0 172,65 150,118 160,64"/>
      <polygon class="fill-slate" points="150,118 162,82 142,155"/>

      <g class="logo">
        <text class="wordmark" x="58" y="33" text-anchor="middle" font-size="7.6">ATELIER MARROW</text>
        <text class="wordmark wordmark__sub" x="58" y="39" text-anchor="middle" font-size="2.8">ARCHITECTURE</text>
      </g>

      <g class="name-badge">
        <rect class="name-pill" x="172" y="18" width="76" height="24" rx="12"/>
        <text class="name" x="210" y="34" text-anchor="middle">Marcus T</text>
      </g>

      <g class="contact">
        <text class="address" x="35" y="72">728 Holloway Ct. NE Atlanta,</text>
        <g class="icon icon--home">
          <rect class="fill-teal" x="110" y="62" width="12" height="12" rx="3"/>
          <path class="icon-glyph" d="M116 64.5 L120 68.2 H119 V71.6 H117 V69.4 H115 V71.6 H113 V68.2 H112 Z"/>
        </g>

        <line class="contact-rule" x1="35" y1="90" x2="107" y2="90"/>
        <g class="icon icon--phone">
          <circle class="fill-paper" cx="116" cy="90" r="6"/>
          <path class="icon-dark" d="M113.6 87.2 l1.2-0.6 1 1.9-0.8 0.6 c0.4 0.9 1 1.6 1.9 2.1 l0.6-0.8 1.9 1-0.6 1.2 c-3.2-0.4-5-2.4-5.2-5.4 z"/>
        </g>

        <line class="contact-rule" x1="35" y1="110" x2="107" y2="110"/>
        <g class="icon icon--pointer">
          <rect class="fill-teal" x="110" y="104" width="12" height="12" rx="3"/>
          <path class="icon-glyph" d="M113 107 L120 109.6 L117 110.6 L116 113.6 Z"/>
        </g>

        <line class="contact-rule" x1="35" y1="130" x2="107" y2="130"/>
        <g class="icon icon--globe">
          <circle class="fill-paper" cx="116" cy="130" r="6"/>
          <circle class="icon-dark" cx="116" cy="130" r="3.6"/>
        </g>
      </g>
    </svg>
  </section>

</main>
</body>
</html>
```